Fiber Optic Internet flyer promotion Winter 2016-2017

I am looking for a marketing flyer that will not be folded, single sided that will advertise a Fiber Optic internet promotion that we are currently running.

The design should be clean, flow well, quickly grab attention, and if a very few short seconds list what the promotion is, and direct them to contact us.

It needs to list a few features of the promotion, but does not need to be in this order and should flow well with the flyer
1.) Fiber Optic Internet
2.) 100 Mbits for $140 /month or 150 Mbits for $190 /month
3.) Free construction cost up to $10,000, limited funds available.
4.) Limited time offer. Must commit before funds run out.

(555) 274-3916, www.kelvoranet.example

Target Market(s)

Small to large business

Industry/Entity Type

Internet Service Provider

Requirements
Must have
• Eye catching appeal. Quickly convey the message of the promotion and our company name and phone number.
Should not have
• Our company is primarily a wireless ISP. This promotion is all about Fiber Optic. I do not want to draw attention to the "wireless" portion of our business with this flyer.

```html
<!DOCTYPE html>
<html lang="en">
<head>
<meta charset="utf-8">
<title>Kelvora Networks – Fiber Optic Internet Flyer</title>
<link rel="stylesheet" href="https://fonts.googleapis.com/css2?family=Archivo+Black&family=Oswald:wght@500;600&family=Roboto:wght@700;900&family=Jost:wght@400;500&display=swap">
<style>
  :root {
    --navy: #0f2a8a;
    --red: #d7202f;
    --white: #ffffff;
    --paper-top: #f4f6f9;
    --paper-bottom: #e3e8ef;
    --stage: #d9dbe0;
    --photo-dark: #0b2a2e;
    --photo-blue: #3550c8;
    --photo-pink: #d2407a;
  }
  html, body {
    margin: 0;
    width: 1041px;
    height: 1200px;
    overflow: hidden;
    background: var(--stage);
  }
  .flyer {
    position: absolute;
    left: 94px;
    top: 5px;
    width: 775px;
    height: 1082px;
    transform: scale(1.1);
    transform-origin: top left;
    background: linear-gradient(160deg, var(--paper-top) 0%, #ffffff 40%, var(--paper-bottom) 100%);
    overflow: hidden;
    font-family: "Roboto", Arial, sans-serif;
  }
  .brand {
    position: absolute;
    left: 73px;
    top: 62px;
    width: 270px;
    text-align: center;
  }
  .brand-mark {
    display: block;
    width: 52px;
    height: 52px;
    margin: 0 auto 10px;
    background: var(--navy);
  }
  .brand-name {
    font-family: "Archivo Black", Arial, sans-serif;
    font-size: 24px;
    line-height: 1;
    color: var(--navy);
    letter-spacing: 0.5px;
  }
  .accent-dot {
    position: absolute;
    left: 520px;
    top: 168px;
    width: 82px;
    height: 82px;
    border-radius: 50%;
    background: var(--red);
    border: 7px solid var(--white);
    box-shadow: 0 0 0 2px var(--red);
    z-index: 3;
  }
  .hero-frame {
    position: absolute;
    left: 65px;
    top: 172px;
    width: 640px;
    height: 525px;
    border: 6px solid var(--red);
    border-radius: 0 30px 30px 0;
    box-sizing: border-box;
    overflow: hidden;
  }
  .hero-photo {
    width: 100%;
    height: 100%;
    background:
      radial-gradient(ellipse at 35% 55%, rgba(90,170,255,0.85) 0%, rgba(90,170,255,0) 28%),
      radial-gradient(ellipse at 75% 35%, var(--photo-pink) 0%, rgba(210,64,122,0) 45%),
      linear-gradient(120deg, var(--photo-dark) 0%, var(--photo-blue) 55%, var(--photo-pink) 100%);
  }
  .speed-inset {
    position: absolute;
    left: 463px;
    top: 580px;
    width: 202px;
    height: 165px;
    border: 5px solid var(--white);
    border-radius: 10px;
    box-sizing: border-box;
    background: radial-gradient(circle at 65% 45%, #3a6fd8 0%, #123070 55%, #8a9099 100%);
    box-shadow: 0 2px 6px rgba(0,0,0,0.3);
  }
  .headline {
    position: absolute;
    left: 73px;
    top: 722px;
    margin: 0;
    font-family: "Archivo Black", Arial, sans-serif;
    font-weight: 400;
    line-height: 1;
    letter-spacing: 1px;
  }
  .headline .line-1 { display: block; color: var(--navy); font-size: 53px; }
  .headline .line-2 { display: block; color: var(--red); font-size: 47px; letter-spacing: 4.5px; margin-top: 6px; }
  .plans { position: absolute; left: 75px; top: 843px; }
  .plan {
    display: flex;
    height: 47px;
    margin-bottom: 17px;
    box-shadow: 0 2px 4px rgba(0,0,0,0.2);
    border-radius: 0 12px 12px 0;
    overflow: hidden;
  }
  .plan-speed {
    width: 175px;
    background: var(--red);
    color: var(--white);
    font-family: "Oswald", Arial, sans-serif;
    font-weight: 500;
    font-size: 22px;
    display: flex;
    align-items: center;
    justify-content: center;
  }
  .plan-price {
    width: 187px;
    background: var(--navy);
    color: var(--white);
    font-family: "Jost", Arial, sans-serif;
    font-size: 24px;
    display: flex;
    align-items: center;
    justify-content: center;
  }
  .plan-price strong { font-family: "Roboto", Arial, sans-serif; font-weight: 700; margin-right: 4px; }
  .promo {
    position: absolute;
    right: 67px;
    top: 763px;
    text-align: right;
    line-height: 1;
  }
  .promo-free { font-family: "Archivo Black", Arial, sans-serif; font-size: 40px; color: var(--red); }
  .promo-cost { font-family: "Oswald", Arial, sans-serif; font-weight: 600; font-size: 21px; color: var(--red); margin-top: 4px; }
  .promo-amount { font-weight: 900; font-size: 21px; color: var(--navy); margin-top: 6px; }
  .promo-amount span { font-size: 28px; }
  .promo-note { font-weight: 700; font-size: 18px; color: var(--red); margin-top: 2px; }
  .partner-badge {
    position: absolute;
    left: 475px;
    top: 900px;
    width: 232px;
    height: 57px;
    background: var(--white);
    border: 1px solid #c9ced6;
    box-sizing: border-box;
  }
  .offer-bar {
    position: absolute;
    left: 30px;
    top: 975px;
    width: 715px;
    height: 41px;
    border: 2px solid var(--red);
    border-radius: 21px;
    box-sizing: border-box;
    background: rgba(255,255,255,0.8);
    display: flex;
    align-items: center;
    justify-content: center;
    font-weight: 700;
    font-size: 19px;
  }
  .offer-bar .offer-lead { color: var(--red); margin-right: 14px; }
  .offer-bar .offer-rest { color: var(--navy); }
  .contact-bar {
    position: absolute;
    left: 0;
    bottom: 0;
    width: 100%;
    height: 50px;
    display: flex;
    font-family: "Jost", Arial, sans-serif;
    font-size: 23px;
    color: var(--white);
  }
  .contact-web {
    width: 458px;
    background: var(--navy);
    display: flex;
    align-items: center;
    justify-content: center;
    gap: 10px;
  }
  .contact-phone {
    flex: 1;
    background: var(--red);
    display: flex;
    align-items: center;
    justify-content: center;
    gap: 12px;
  }
  .dots { display: flex; gap: 6px; margin: 0 10px; }
  .dots i { width: 9px; height: 9px; border-radius: 50%; background: var(--white); display: block; }
  .dots i.faint { opacity: 0.45; }
  .icon { width: 24px; height: 24px; }
</style>
</head>
<body>
  <main class="flyer">
    <header class="brand">
      <span class="brand-mark"></span>
      <div class="brand-name">KELVORA NETWORKS</div>
    </header>

    <div class="hero-frame">
      <div class="hero-photo" role="img" aria-label="Close-up photo of a network cable plug in front of glowing fiber optic strands"></div>
    </div>
    <div class="accent-dot"></div>
    <div class="speed-inset" role="img" aria-label="Photo of a speedometer gauge measuring Mbps"></div>

    <h1 class="headline">
      <span class="line-1">FIBER OPTIC</span>
      <span class="line-2">INTERNET</span>
    </h1>

    <section class="plans">
      <div class="plan">
        <div class="plan-speed">100 MBITS FOR</div>
        <div class="plan-price"><strong>$140</strong>/month</div>
      </div>
      <div class="plan">
        <div class="plan-speed">150 MBITS FOR</div>
        <div class="plan-price"><strong>$190</strong>/month</div>
      </div>
    </section>

    <section class="promo">
      <div class="promo-free">FREE</div>
      <div class="promo-cost">CONSTRUCTION COST</div>
      <div class="promo-amount">up to <span>$10,000</span></div>
      <div class="promo-note">limited funds available</div>
    </section>

    <div class="partner-badge"></div>

    <div class="offer-bar">
      <span class="offer-lead">LIMITED TIME OFFER.</span>
      <span class="offer-rest">Must commit before funds run out.</span>
    </div>

    <footer class="contact-bar">
      <div class="contact-web">
        <span class="dots"><i class="faint"></i><i class="faint"></i><i></i></span>
        <svg class="icon" viewBox="0 0 24 24" fill="none" stroke="#fff" stroke-width="1.8">
          <circle cx="12" cy="12" r="9.5"/>
          <ellipse cx="12" cy="12" rx="4.5" ry="9.5"/>
          <line x1="2.5" y1="12" x2="21.5" y2="12"/>
          <path d="M4.5 7h15M4.5 17h15"/>
        </svg>
        <span>www.kelvoranet.example</span>
        <span class="dots"><i></i><i class="faint"></i><i class="faint"></i></span>
      </div>
      <div class="contact-phone">
        <svg class="icon" viewBox="0 0 24 24" fill="none" stroke="#fff" stroke-width="1.8">
          <circle cx="12" cy="12" r="10.5"/>
          <path d="M8.2 6.5l1.8-.3 1.2 2.8-1.3 1.1c.6 1.5 1.6 2.6 3.1 3.2l1.1-1.3 2.8 1.2-.3 1.8c-.2.8-1 1.2-1.8 1.1-4-.6-7.2-3.8-7.8-7.8-.1-.8.4-1.6 1.2-1.8z" fill="#fff" stroke="none"/>
        </svg>
        <span>(555) 274-3916</span>
      </div>
    </footer>
  </main>
</body>
</html>
```